K.R.O.U.B.S. Content Framework Infographic

I am looking to take my basic infographic to the next level. I need to to translate the content marketing concept that is outlined in the uploaded file. I have attached the content and the image I would like used. I am not stuck on the colors represented in the image but do want to see a variety of options.

Target Market(s)

Companies that are looking for a content marketing strategy, SEO Agencies, marketing agencies

Industry/Entity Type

Digital marketing, SEO

Font styles to use
Other font styles liked:
• arial, calibri are fine

Colors
0054AA
0677BA
7BADD7
CADEEF
E8F1F8
0094D4
00A9DD
6FCCEA
C7EBF8
E9F6FB
00AB8E
00BBA5
67D7C9
C6EFE9
E9F9F6
59FF00
82FF00
B8FF75
E3FFCB
F4FFEA
EE7325
F08F49
F5BC92
FAE3D3
FDF4ED
EB3D1F
EC4F4E
F09395
F8D3D4
FCEDEE

Requirements
Must have
• The image that I provided with the content breakdown with section connectors to the image
Nice to have
• a few different way to present the data

```html
<!DOCTYPE html>
<html lang="en">
<head>
<meta charset="utf-8">
<title>K.R.O.U.B.S. Content Framework</title>
<link rel="stylesheet" href="https://fonts.googleapis.com/css2?family=Poppins:wght@600;700&family=Open+Sans:wght@400&display=swap">
<style>
  :root {
    --page-bg: #e8e8e8;
    --card-bg: #ffffff;
    --header-bg: #444444;
    --header-stripe: #9a9a9a;
    --body-text: #666666;
    --blue: #1ea6dd;
    --green: #8cc63f;
    --red: #e8402a;
    --purple: #9b1e6e;
    --brown: #7a5132;
    --navy: #2b3a8c;
    --hex-grey: #d2d2d2;
    --ring-grey: #cfcfcf;
  }
  * { box-sizing: border-box; margin: 0; padding: 0; }
  html, body { width: 1200px; height: 1200px; overflow: hidden; }
  body { background: var(--page-bg); position: relative; font-family: "Open Sans", Arial, sans-serif; }

  .infographic {
    position: absolute; left: 0; top: 171px;
    width: 1310px; height: 936px;
    background: var(--card-bg);
    transform: scale(0.91603); transform-origin: top left;
  }
  .masthead {
    position: absolute; left: 0; top: 0; width: 100%; height: 172px;
    background: var(--header-bg); color: #fff; text-align: center;
    border-bottom: 12px solid var(--header-stripe);
    height: 184px;
  }
  .masthead__title {
    font-family: "Poppins", Arial, sans-serif; font-weight: 700;
    font-size: 27px; line-height: 1; padding-top: 19px;
  }
  .masthead__intro { font-size: 12.5px; line-height: 17px; margin-top: 20px; }

  .pillar { position: absolute; width: 260px; }
  .pillar__title {
    font-family: "Poppins", Arial, sans-serif; font-weight: 700;
    font-size: 20px; line-height: 24px; margin-bottom: 6px;
  }
  .pillar__text { font-size: 12.5px; line-height: 17px; color: var(--body-text); }
  .pillar--left { text-align: right; }
  .pillar--right { text-align: left; }

  .pillar--expertise { left: 83px; top: 208px; }
  .pillar--engagement { left: 55px; top: 399px; }
  .pillar--multimedia { left: 83px; top: 648px; }
  .pillar--experience { left: 957px; top: 208px; }
  .pillar--authority { left: 999px; top: 399px; }
  .pillar--trust { left: 957px; top: 648px; }

  .pillar--expertise .pillar__title { color: var(--blue); }
  .pillar--engagement .pillar__title { color: var(--green); }
  .pillar--multimedia .pillar__title { color: var(--red); }
  .pillar--experience .pillar__title { color: var(--purple); }
  .pillar--authority .pillar__title { color: var(--brown); }
  .pillar--trust .pillar__title { color: var(--navy); }

  .cycle { position: absolute; left: 0; top: 0; width: 1310px; height: 936px; }
  .badge-letter {
    font-family: "Poppins", Arial, sans-serif; font-weight: 700; font-size: 26px;
    text-anchor: middle; dominant-baseline: central;
  }

  .hero-animal {
    position: absolute; left: 433px; top: 383px; width: 447px; height: 265px;
    border-radius: 38% 46% 30% 30% / 40% 48% 34% 34%;
    background: linear-gradient(90deg, var(--red) 0%, #4fb0e6 30%, #8cc63f 45%, var(--purple) 62%, var(--navy) 82%);
  }
</style>
</head>
<body>
  <main class="infographic">
    <header class="masthead">
      <h1 class="masthead__title">Putting K.R.O.U.B.S. on the bone for the User &amp; Searchly To Chew on</h1>
      <p class="masthead__intro">
        In SEO content is still king.&nbsp; What has changed with content is not the content but the delivery of that content.<br>
        People these days are consuming content in so many different places &amp; formats that it makes it difficult to create engaging content that ranks and converts.<br>
        Some people prefer to continue reading webpages to find the information they are looking for.&nbsp; Some prefer to see the pictures because they are more visual than contextual.<br>
        Others would prefer to just watch video on ViewTube or other online video platforms, and in some cases it is more of an auditory way such as podcast &amp; streaming radio platforms.<br>
        This infographic will breakdown how all of the pieces fit together to get “K.R.O.U.B.S.” on the bone of content.
      </p>
    </header>

    <svg class="cycle" viewBox="0 0 1310 936" aria-hidden="true">
      <!-- section dividers -->
      <g stroke-width="2.5">
        <line x1="380" y1="218" x2="380" y2="328" stroke="var(--blue)"/>
        <line x1="343" y1="466" x2="343" y2="576" stroke="var(--green)"/>
        <line x1="380" y1="713" x2="380" y2="823" stroke="var(--red)"/>
        <line x1="930" y1="218" x2="930" y2="328" stroke="var(--purple)"/>
        <line x1="967" y1="466" x2="967" y2="576" stroke="var(--brown)"/>
        <line x1="930" y1="713" x2="930" y2="823" stroke="var(--navy)"/>
      </g>

      <!-- backdrop hexagon -->
      <polygon points="455,516 555,333 755,333 855,516 755,699 555,699" fill="none" stroke="var(--hex-grey)" stroke-width="22" stroke-linejoin="miter"/>

      <!-- ring segments -->
      <g fill="none" stroke-width="2.5">
        <path d="M527,313 A242,242 0 0 1 783,313" stroke="var(--blue)"/>
        <path d="M783,313 A242,242 0 0 1 897,518" stroke="var(--purple)"/>
        <path d="M897,518 A242,242 0 0 1 783,723" stroke="var(--brown)"/>
        <path d="M783,723 A242,242 0 0 1 527,723" stroke="var(--ring-grey)" stroke-width="1.2"/>
        <path d="M527,723 A242,242 0 0 1 413,518" stroke="var(--red)"/>
        <path d="M413,518 A242,242 0 0 1 527,313" stroke="var(--green)"/>
      </g>

      <!-- flow arrows -->
      <polygon points="-6,-5 6,0 -6,5" fill="var(--blue)" transform="translate(655,276)"/>
      <polygon points="-6,-5 6,0 -6,5" fill="var(--purple)" transform="translate(867,401) rotate(61)"/>
      <polygon points="-6,-5 6,0 -6,5" fill="var(--brown)" transform="translate(867,635) rotate(119)"/>
      <polygon points="-6,-5 6,0 -6,5" fill="var(--red)" transform="translate(443,635) rotate(241)"/>
      <polygon points="-6,-5 6,0 -6,5" fill="var(--green)" transform="translate(443,401) rotate(-61)"/>

      <!-- badge connectors -->
      <g stroke-width="2.5">
        <line x1="502" y1="281" x2="527" y2="313" stroke="var(--blue)"/>
        <line x1="808" y1="281" x2="783" y2="313" stroke="var(--purple)"/>
        <line x1="472" y1="780" x2="527" y2="723" stroke="var(--red)"/>
        <line x1="841" y1="780" x2="783" y2="723" stroke="var(--navy)"/>
      </g>

      <!-- letter badges -->
      <g stroke-width="2.5" fill="#fff">
        <circle cx="502" cy="281" r="24" stroke="var(--blue)"/>
        <circle cx="808" cy="281" r="24" stroke="var(--purple)"/>
        <circle cx="926" cy="516" r="24" stroke="var(--brown)"/>
        <circle cx="841" cy="780" r="24" stroke="var(--navy)"/>
        <circle cx="472" cy="780" r="24" stroke="var(--red)"/>
        <circle cx="383" cy="516" r="24" stroke="var(--green)"/>
      </g>
      <text class="badge-letter" x="502" y="282" fill="var(--blue)">E</text>
      <text class="badge-letter" x="808" y="282" fill="var(--purple)">E</text>
      <text class="badge-letter" x="926" y="517" fill="var(--brown)">A</text>
      <text class="badge-letter" x="841" y="781" fill="var(--navy)">T</text>
      <text class="badge-letter" x="472" y="781" fill="var(--red)">M</text>
      <text class="badge-letter" x="383" y="517" fill="var(--green)">E</text>
    </svg>

    <div class="hero-animal" role="img" aria-label="Illustration of a pig divided into coloured cuts, each cut marked with an icon for one framework pillar"></div>

    <section class="pillar pillar--left pillar--expertise">
      <h2 class="pillar__title">Expertise</h2>
      <p class="pillar__text">“Expertise” refers to the content writer’s<br>level of knowledge or skill in a specific<br>subject area that is relevant to the user’s<br>search query. High-quality content should<br>be created by someone with relevant<br>expertise in the topic being discussed.</p>
    </section>

    <section class="pillar pillar--left pillar--engagement">
      <h2 class="pillar__title">Engagement</h2>
      <p class="pillar__text">“Engagement” is essential for views and<br>conversion as it keeps readers locked in<br>on content to the point that they are<br>more likely to move through the<br>website experience and at least<br>consider the value offered in the<br>minutes, hours, days, and weeks that<br>follow their website visit.</p>
    </section>

    <section class="pillar pillar--left pillar--multimedia">
      <h2 class="pillar__title">Multimedia</h2>
      <p class="pillar__text">“Multimedia”consists of infographics,<br>specific images, embedded videos, and<br>other types content aside from the written<br>word.&nbsp; By doing this you provide the same<br>content to audiences that differ based on<br>how they choose to consume content.<br>Online content marketing with multimedia<br>is highly engaging as it presents desired<br>information in a multifaceted but&nbsp; direct and</p>
    </section>

    <section class="pillar pillar--right pillar--experience">
      <h2 class="pillar__title">Experience</h2>
      <p class="pillar__text">“Experience” in short means that Searchly<br>values firsthand or life experience of the<br>author on the topic a page is about. It is<br>important because often searchers want to<br>know first-hand information before they<br>decide to purchase something or use a<br>certain service.</p>
    </section>

    <section class="pillar pillar--right pillar--authority">
      <h2 class="pillar__title">Authoritativeness</h2>
      <p class="pillar__text">“Authoritativeness” refers to the<br>credibility of the content and the<br>website it is hosted on.<br>Authoritativeness can be established<br>through the quality of the content, the<br>site’s reputation, author’s reputation,<br>external links &amp; content citations, and<br>the credentials of the content creator.</p>
    </section>

    <section class="pillar pillar--right pillar--trust">
      <h2 class="pillar__title">Trustworthiness</h2>
      <p class="pillar__text">“Trustworthiness” is the final result of doing<br>all of the above.&nbsp; If you can write content<br>that is helpful, knowledge, first hand based<br>on experience from someone who is an<br>expert in their field, you get the trust of<br>users consuming your content.&nbsp; If you can<br>gain the user’s trust about your content,<br>Searchly and other search engines will “Trust”<br>you and will provide you with the organic<br>visibility we all strive for..</p>
    </section>
  </main>
</body>
</html>
```